Dorian "Strike Up Tomorrow"

Hello, looking for a flyer design for our band project, we are an Marlo Tribute artist seeking school band programs to work together on a fundraiser where the school band will join our band for 1 night and be part of the show. Red and Black should be the most dominant colors in the flyer. There is a flyer being used by friends of ours for a similar project it can be found at http://www.copperfolkrevue.com/qzrt.html

the text for the flyer is as follows, again very similar to what the Quillmarks guys are using

Dorian Pell - Marlo Tribute Artist presents

"Strike Up Tomorrow"

Bring Marlo Tribute Artist - Dorian Pell from Lanternglow Theatre in Pigeon Forge, TN to your school to perform with your bands, orchestras, and choirs

Dorian has launched a new fundraising program for schools to keep music programs alive in our schools

What you need to know anout this project

* There is absolutely no cost to the school
* Charts to the Marlo songs will be provided
* Your students perform with Dorian Pell & his band during a special section of the show
* Dorian is available for all local media interviews, and assistance in the promotion of the event on behalf of your program
*A portion of the proceeds are shared with the music program

The concert is educational and entertaining, spanning from the early "bubble gum" years through the Vegas era

Great exposure for your school music program to a whole new audience

Wonderful experience for students that is exciting and FUN!!

_________________

I would prefer this design to be on 8.5 x 11 (if longer page is needed, or front and back is ok also)

please find graphics attached , please feel free to use as few or as many as you would like.

Thanks

```html
<!DOCTYPE html>
<html lang="en">
<head>
<meta charset="utf-8">
<title>Strike Up Tomorrow – Dorian Pell</title>
<link rel="stylesheet" href="https://fonts.googleapis.com/css2?family=Bebas+Neue&family=Questrial&display=swap">
<style>
  :root {
    --red: #f00d0d;
    --black: #000000;
    --white: #ffffff;
    --paper: #ffffff;
    --photo-dark: #5a0000;
    --photo-mid: #c40000;
    --photo-light: #ff6a5a;
  }
  * { margin: 0; padding: 0; box-sizing: border-box; }
  html, body { width: 900px; height: 1200px; overflow: hidden; background: var(--paper); }
  .flyer { position: relative; width: 900px; height: 1200px; background: var(--paper); overflow: hidden; }
  .flyer__board { position: absolute; left: 20px; top: 35px; width: 863px; height: 1135px; background: var(--black); }
  .rule { position: absolute; top: 0; width: 8px; background: var(--red); }
  .rule--main { left: 284px; height: 1200px; }
  .rule--photo-a { left: 487px; height: 345px; }
  .rule--photo-b { left: 680px; height: 345px; }
  .photo { position: absolute; top: 45px; height: 300px; }
  .photo--stage { left: 296px; width: 187px; background: radial-gradient(ellipse at 55% 50%, var(--photo-light), var(--photo-mid) 35%, var(--photo-dark) 80%); }
  .photo--sing { left: 499px; width: 177px; background: radial-gradient(ellipse at 45% 55%, var(--photo-light), var(--photo-mid) 45%, var(--photo-dark) 90%); }
  .photo--pose { left: 692px; width: 176px; background: radial-gradient(ellipse at 50% 60%, var(--photo-light), var(--photo-mid) 45%, var(--photo-dark) 90%); }

  .title { position: absolute; left: 34px; top: 0; width: 240px; height: 420px; color: var(--red); font-family: "Bebas Neue", sans-serif; font-weight: 400; text-align: center; }
  .title__line { position: absolute; left: 0; width: 240px; line-height: 1; white-space: nowrap; transform-origin: 50% 0; }
  .title__line--strike { top: 28px; font-size: 108px; transform: scaleY(1.4); }
  .title__line--up { top: 178px; font-size: 46px; }
  .title__line--tomorrow { top: 228px; font-size: 66px; transform: scaleY(2.4); }

  .content { position: absolute; left: 313px; top: 378px; width: 500px; color: var(--white); }
  .presenter { font-family: "Bebas Neue", sans-serif; font-size: 28px; line-height: 0.95; }
  .headline { font-family: "Bebas Neue", sans-serif; font-weight: 400; font-size: 50px; line-height: 0.85; margin-top: 14px; }
  .body { font-family: "Questrial", sans-serif; font-size: 19px; line-height: 1.05; width: 465px; }
  .intro { margin-top: 8px; width: 185px; }
  .lead { font-family: "Bebas Neue", sans-serif; font-size: 26px; line-height: 1; margin-top: 16px; }
  .need { margin-top: 12px; }
  .points { list-style: none; margin-top: 18px; }
  .points li { position: relative; padding-left: 18px; }
  .points li::before { content: ""; position: absolute; left: 0; top: 6px; width: 9px; height: 9px; border-radius: 50%; background: var(--red); }
  .para { margin-top: 20px; }
  .closer { font-family: "Bebas Neue", sans-serif; font-size: 30px; line-height: 0.92; margin-top: 20px; }
  .brand { position: absolute; left: 80px; top: 1070px; color: var(--white); font-family: "Bebas Neue", sans-serif; font-size: 50px; letter-spacing: 2px; }
</style>
</head>
<body>
<div class="flyer">
  <div class="flyer__board"></div>
  <div class="photo photo--stage" role="img" aria-label="Red-toned photo of Dorian Pell performing on stage in a white jumpsuit"></div>
  <div class="photo photo--sing" role="img" aria-label="Red-toned close photo of Dorian Pell singing into a microphone"></div>
  <div class="photo photo--pose" role="img" aria-label="Red-toned photo of Dorian Pell striking a pose with raised arm"></div>
  <div class="rule rule--main"></div>
  <div class="rule rule--photo-a"></div>
  <div class="rule rule--photo-b"></div>

  <h1 class="title">
    <span class="title__line title__line--strike">Strike</span>
    <span class="title__line title__line--up">Up</span>
    <span class="title__line title__line--tomorrow">Tomorrow</span>
  </h1>

  <div class="content">
    <p class="presenter">Dorian Pell<br>Marlo Tribute Artist Presents:</p>
    <h2 class="headline">Bring Marlo Tribute Artist<br>Dorian Pell</h2>
    <p class="body intro">To your school to perform with your bands, orchestras, and choirs</p>
    <p class="lead">Dorian has launched a new fundraising program for<br>schools to keep music programs alive in our schools</p>
    <p class="body need">What you need to know about this project:</p>
    <ul class="body points">
      <li>There is absolutely no cost to the school</li>
      <li>Charts to the Marlo songs will be provided</li>
      <li>Your students perform with Dorian Pell &amp;<br>his band during a special section of the show</li>
      <li>Dorian is available for all local media<br>interviews, and assistance in the promotion<br>of the event on behalf of your program</li>
      <li>A portion of the proceeds are shared with<br>the music program</li>
    </ul>
    <p class="body para">The concert is educational and entertaining,<br>spanning from the early "bubble gum" years<br>through the Vegas era</p>
    <p class="body para">Great exposure for your school music<br>program to a whole new audience</p>
    <p class="closer">Wonderful experience for students that<br>is exciting and fun!!</p>
  </div>

  <div class="brand">DORIAN</div>
</div>
</body>
</html>
```